Korvane Stratus Product Brochure

We need a brochure designed (multiple pages) representing the premium range our Korvane Point of Sale products and accessories. Our current range of products can be viewed at www.korvanepos.co. I've attached a couple of Korvane product brochures as a reference. We need a "premium" version of these brochures preserving some of the Korvane branding features (Blue swirl, blue colour, fonts etc.). The new brochures will be for our premium branch of Korvane - called Korvane Stratus (logo attached). We are after a more "expensive" "Halvorsen Drake" kind of look and feel for the Korvane Stratus Brochures. The content for the brochure (Packaged file - Korvane Stratus Qx+ Poing of Sale Terminal) is attached. Feel free to use the images & text but the overall look and feel of this brochure need to change.
So just to summarise, the new brochures need to be consistent with our current Korvane branding but have a more "polished" "expensive" "premium look. Selected design needs to be submitted in an InDesign format.
Target Market(s)
Point of Sale customers in the Retail & Hospitality space
Look and feel

```html
<!DOCTYPE html>
<html lang="en">
<head>
<meta charset="utf-8">
<title>Korvane Stratus Product Brochure</title>
<link href="https://fonts.googleapis.com/css2?family=Montserrat:wght@400;600;700;800&family=Open+Sans:wght@400;600&display=swap" rel="stylesheet">
<style>
  :root{
    --stage:#e9eaec;
    --cover-dark:#3d4650;
    --cover-mid:#4b5561;
    --paper:#f4f5f6;
    --ink:#2b2f35;
    --muted:#6b727b;
    --blue:#1f8fd6;
    --blue-light:#8fd0f5;
    --blue-deep:#0b4f8a;
    --white:#ffffff;
    --rule:#5a6470;
  }
  *{box-sizing:border-box;margin:0;padding:0}
  html,body{width:857px;height:1200px;overflow:hidden;background:var(--stage)}
  body{font-family:"Open Sans",Arial,sans-serif;color:var(--ink);position:relative}
  .spread{position:absolute;left:48px;width:760px;height:537px;display:flex;box-shadow:0 6px 18px rgba(0,0,0,.18)}
  .spread--outside{top:38px}
  .spread--inside{top:625px}
  .page{position:relative;width:380px;height:537px;overflow:hidden}

  /* outside */
  .back-cover,.front-cover{background:linear-gradient(160deg,var(--cover-mid),var(--cover-dark));color:var(--white)}
  .back-cover{border-right:1px solid #353d46}
  .logo-plate{position:absolute;left:28px;top:30px;width:150px;height:46px;background:var(--white);display:flex;align-items:center;gap:7px;padding:0 12px;white-space:nowrap}
  .logo-plate .mark{width:10px;height:10px;background:var(--blue);flex:none}
  .logo-plate span{font-family:"Montserrat",sans-serif;font-weight:700;font-size:11px;color:var(--cover-dark);letter-spacing:.5px}
  .spec-title{position:absolute;left:28px;top:96px;font-family:"Montserrat",sans-serif;font-weight:700;font-size:10px;letter-spacing:1px;text-transform:uppercase;color:var(--blue-light)}
  .spec-table{position:absolute;left:28px;top:116px;width:324px;border-collapse:collapse;font-size:8px}
  .spec-table td{padding:6px 6px;border-bottom:1px solid var(--rule)}
  .spec-table td:first-child{width:90px;font-weight:600;color:var(--blue-light);background:rgba(255,255,255,.05)}
  .back-url{position:absolute;left:28px;bottom:24px;font-size:8px;color:#b8c0c8;letter-spacing:.5px}

  .front-label{position:absolute;right:28px;top:118px;font-family:"Montserrat",sans-serif;font-size:8px;font-weight:600;letter-spacing:1.5px;text-transform:uppercase;color:#c9d0d7;text-align:right}
  .front-headline{position:absolute;right:28px;top:136px;width:190px;font-family:"Montserrat",sans-serif;font-weight:800;font-size:17px;line-height:1.25;text-align:right;text-transform:uppercase}
  .front-intro{position:absolute;right:28px;top:204px;width:170px;font-size:8px;line-height:1.5;text-align:right;color:#c9d0d7}
  .product-shot{position:absolute;left:40px;top:250px;width:200px;height:170px;background:radial-gradient(ellipse at 55% 45%,#1c2127 0%,#2c333b 55%,rgba(61,70,80,0) 75%)}
  .swirl{position:absolute;background:linear-gradient(100deg,rgba(143,208,245,.0) 0%,rgba(143,208,245,.55) 30%,var(--blue) 60%,var(--blue-deep) 100%)}
  .swirl--back{left:0;bottom:0;width:380px;height:70px;opacity:.5;clip-path:polygon(0 60%,40% 30%,100% 0,100% 100%,0 100%)}
  .swirl--front{left:0;bottom:0;width:380px;height:120px;clip-path:polygon(0 45%,30% 70%,65% 35%,100% 55%,100% 100%,0 100%)}
  .front-brand{position:absolute;right:28px;bottom:24px;display:flex;align-items:center;gap:6px;font-family:"Montserrat",sans-serif;font-weight:700;font-size:14px;color:var(--white)}
  .front-brand .mark{width:9px;height:9px;border-radius:50%;background:var(--white)}

  /* inside */
  .inside-left,.inside-right{background:var(--paper)}
  .inside-left{border-right:1px solid #d9dcdf}
  .swirl--inside{left:0;top:0;width:380px;height:95px;clip-path:polygon(0 0,100% 0,100% 20%,60% 55%,25% 80%,0 100%)}
  .section-head{font-family:"Montserrat",sans-serif;font-weight:700;font-size:10px;line-height:1.3;text-transform:uppercase;color:var(--blue)}
  .section-text{font-size:7.5px;line-height:1.5;color:var(--muted);margin-top:5px}
  .block{position:absolute}
  .photo{position:absolute;background:linear-gradient(150deg,#d7dadd,#9aa1a8 60%,#3a4047)}
  .inside-url{position:absolute;left:28px;bottom:20px;font-size:7px;color:var(--muted)}
  .folio-brand{position:absolute;right:28px;top:22px;font-family:"Montserrat",sans-serif;font-weight:700;font-size:9px;color:var(--ink);display:flex;gap:5px;align-items:center}
  .folio-brand .mark{width:7px;height:7px;background:var(--blue)}
  .hub-lines{position:absolute;left:150px;top:40px}
</style>
</head>
<body>

<section class="spread spread--outside">
  <article class="page back-cover">
    <div class="logo-plate"><i class="mark"></i><span>Korvane Stratus</span></div>
    <h3 class="spec-title">Technical Specifications</h3>
    <table class="spec-table">
      <tr><td>Processor</td><td>Quad-Core CPU</td></tr>
      <tr><td>Memory</td><td>8GB DDR4</td></tr>
      <tr><td>Storage</td><td>128GB SSD</td></tr>
      <tr><td>Display</td><td>15.6" Touch</td></tr>
      <tr><td>System</td><td>Embedded OS</td></tr>
      <tr><td>Ports</td><td>USB LAN COM</td></tr>
      <tr><td>Power</td><td>65W Adapter</td></tr>
      <tr><td>Finish</td><td>Black Aluminium</td></tr>
    </table>
    <div class="swirl swirl--back" role="img" aria-label="Blue brand swirl"></div>
    <p class="back-url">www.korvanepos.co</p>
  </article>

  <article class="page front-cover">
    <p class="front-label">Korvane Stratus Qx+</p>
    <h1 class="front-headline">Sleek and versatile experience</h1>
    <p class="front-intro">A refined terminal built for busy counters, pairing slim design with lasting performance.</p>
    <div class="product-shot" role="img" aria-label="Point of sale terminal on a swivel stand"></div>
    <div class="swirl swirl--front" role="img" aria-label="Blue brand swirl"></div>
    <div class="front-brand"><i class="mark"></i>korvane</div>
  </article>
</section>

<section class="spread spread--inside">
  <article class="page inside-left">
    <div class="swirl swirl--inside" role="img" aria-label="Blue brand swirl"></div>
    <div class="block" style="left:28px;top:110px;width:150px">
      <h2 class="section-head">Premium design for modern service</h2>
      <p class="section-text">Slim aluminium body and adjustable stand suit any counter.</p>
    </div>
    <div class="photo" style="left:200px;top:105px;width:150px;height:110px" role="img" aria-label="Terminal shown from the side"></div>
    <div class="photo" style="left:28px;top:235px;width:150px;height:120px" role="img" aria-label="Terminal with rear customer display"></div>
    <div class="photo" style="left:200px;top:240px;width:150px;height:110px" role="img" aria-label="Terminal folded flat"></div>
    <div class="block" style="left:28px;top:380px;width:150px">
      <h2 class="section-head">Multiple display options</h2>
      <p class="section-text">Add a second screen for customers or kitchen staff.</p>
    </div>
    <div class="photo" style="left:200px;top:375px;width:150px;height:120px" role="img" aria-label="Dual screen terminal set-up"></div>
    <p class="inside-url">www.korvanepos.co</p>
  </article>

  <article class="page inside-right">
    <div class="folio-brand"><i class="mark"></i>korvane</div>
    <svg class="hub-lines" width="200" height="120" viewBox="0 0 200 120" aria-hidden="true">
      <g stroke="#9aa1a8" stroke-width="1" fill="none">
        <line x1="100" y1="60" x2="30" y2="20"/><line x1="100" y1="60" x2="170" y2="20"/>
        <line x1="100" y1="60" x2="30" y2="100"/><line x1="100" y1="60" x2="170" y2="100"/>
      </g>
    </svg>
    <div class="photo" style="left:225px;top:80px;width:60px;height:45px" role="img" aria-label="Terminal at centre of peripherals"></div>
    <div class="photo" style="left:165px;top:45px;width:34px;height:28px" role="img" aria-label="Receipt printer"></div>
    <div class="photo" style="left:310px;top:45px;width:34px;height:28px" role="img" aria-label="Handheld scanner"></div>
    <div class="photo" style="left:165px;top:130px;width:34px;height:28px" role="img" aria-label="Cash drawer"></div>
    <div class="photo" style="left:310px;top:130px;width:34px;height:28px" role="img" aria-label="Card reader"></div>
    <div class="block" style="left:28px;top:60px;width:125px">
      <h2 class="section-head">Wide range of peripherals to suit your business</h2>
      <p class="section-text">Printers, drawers and scanners connect in seconds.</p>
    </div>
    <div class="photo" style="left:28px;top:200px;width:150px;height:120px" role="img" aria-label="Terminal with customer facing display"></div>
    <div class="block" style="left:200px;top:215px;width:150px">
      <h2 class="section-head">Customer display</h2>
      <p class="section-text">Show totals and promotions at checkout.</p>
    </div>
    <div class="block" style="left:28px;top:350px;width:150px">
      <h2 class="section-head">15.6 inch touch screen</h2>
      <p class="section-text">Bright, responsive glass for fast orders.</p>
    </div>
    <div class="photo" style="left:200px;top:345px;width:150px;height:150px" role="img" aria-label="Front view of touch screen terminal"></div>
  </article>
</section>

</body>
</html>
```